Root Crate Filtration Label Design

Need a sticker or label design for our Root Crate to fit an 8x6" area.

UPDATE 9/21/2015:
We eliminated some text and would like to see only the following on the label:

Root Crate Contains:

- Terrestrial Soil
- Lake Sediment
- Organic Matter
- Natural Bacteria
- Minerals & Trace Elements

"STAY RIVER CALM"

We would love to see an illustration of graphic of the outline of our Root Crate (Black plastic box) showing the soil on the inside which is brown and a thin layer of foam on top of the soil inside the box. On top of the box a layer of natural gravel and the plant roots shown growing through the gravel into the soil inside of the box.

Watch this video to get an idea of how the Root Crate fits in an aquarium under a layer of gravel: https://www.clipvaultly.com/watch?t=92&v=qrTm4kLx8Wd
Updates

Target Market(s)

Customers in Retail Stores

Industry/Entity Type

Pet

Font styles to use
Sans Serif

Colors
9bcb3c
0393ce
0255a3
33b8a4
cadf82
add136
86cfc7
cfeae6
eaf2ce

Requirements
Must have
• Stay River Calm and most of the Text - Text can be changed slightly or simplified
Nice to have
• I have attached a picture of a "FRESHWATER Fish Scene" we like.
Should not have
• NOT Too busy - Trying to keep it as simple as possible - Natural Earthy Colors - Realistic Drawings. DO NOT ADD Marine Fish or other MARINE life. This is strictly for FRESHWATER FISH.

```html
<!DOCTYPE html>
<html lang="en">
<head>
<meta charset="utf-8">
<title>Root Crate Filtration Label</title>
<link rel="stylesheet" href="https://fonts.googleapis.com/css2?family=Roboto:ital,wght@0,400;0,700;0,900;1,900&family=Roboto+Condensed:wght@700&display=swap">
<style>
  :root {
    --label-green: #a9d23a;
    --outline: #111111;
    --ink: #1b1b1b;
    --brand-blue: #0f63b6;
    --accent-blue: #0393ce;
    --panel: #eaf2ce;
    --white: #ffffff;
  }
  * { margin: 0; padding: 0; box-sizing: border-box; }
  html, body { width: 784px; height: 1200px; overflow: hidden; background: var(--white); }
  .canvas { position: relative; width: 784px; height: 1200px; font-family: "Roboto", sans-serif; color: var(--ink); }
  .label-shapes { position: absolute; inset: 0; }
  .label-body { fill: var(--label-green); stroke: #8fa94a; stroke-width: 1; }
  .label-frame { fill: none; stroke: var(--outline); stroke-width: 3; }

  .front-title { position: absolute; left: 142px; width: 499px; text-align: center; white-space: nowrap; line-height: 1; }
  .brand-name { top: 205px; font-weight: 900; font-size: 70px; letter-spacing: 1px; color: var(--brand-blue); }
  .product-type { top: 305px; font-weight: 900; font-style: italic; font-size: 74px; letter-spacing: 1px; color: var(--ink); }

  .contents-heading { position: absolute; top: 700px; left: 125px; width: 533px; text-align: center; font-weight: 700; font-size: 30px; }
  .contents-panel { position: absolute; top: 745px; left: 236px; width: 318px; height: 118px; background: var(--panel); padding: 8px 14px; }
  .contents-list { list-style: none; }
  .contents-list li { font-size: 13px; line-height: 18px; padding: 3px 0 2px; border-bottom: 2px solid var(--ink); white-space: nowrap; }
  .contents-list li:last-child { border-bottom: none; }

  .product-blurb { position: absolute; top: 880px; left: 150px; width: 484px; text-align: center; font-size: 15px; line-height: 20px; }
  .product-blurb .highlight { color: var(--accent-blue); font-weight: 700; }
  .contact-line { position: absolute; top: 950px; left: 125px; width: 533px; text-align: center; font-size: 13px; word-spacing: 6px; white-space: nowrap; }
  .slogan { position: absolute; top: 985px; left: 125px; width: 533px; text-align: center; white-space: nowrap; font-family: "Roboto Condensed", sans-serif; font-weight: 700; font-size: 46px; letter-spacing: 3px; color: var(--white); }
  .slogan .slogan-accent { color: var(--accent-blue); }
</style>
</head>
<body>
<main class="canvas">
  <svg class="label-shapes" width="784" height="1200" viewBox="0 0 784 1200" aria-hidden="true">
    <path class="label-body" d="M125 80 C270 20 430 120 658 55 L658 520 C430 585 270 485 125 548 Z"/>
    <path class="label-frame" d="M142 96 C280 42 432 138 641 76 L641 505 C432 565 280 468 142 528 Z"/>
    <path class="label-body" d="M125 660 C270 600 430 700 658 635 L658 1100 C430 1165 270 1065 125 1128 Z"/>
    <path class="label-frame" d="M142 676 C280 622 432 718 641 656 L641 1085 C432 1145 280 1048 142 1108 Z"/>
  </svg>

  <section class="label-front">
    <div class="front-title brand-name">ROOT CRATE</div>
    <div class="front-title product-type">FILTRATION</div>
  </section>

  <section class="label-back">
    <h2 class="contents-heading">Biological filter contains</h2>
    <div class="contents-panel">
      <ul class="contents-list">
        <li>Terrestrial Soil</li>
        <li>Lake Sediment</li>
        <li>Organic Matter</li>
        <li>Natural Bacteria, Minerals &amp; Trace Elements</li>
      </ul>
    </div>
    <p class="product-blurb">A Natural Approach for Thriving Fish &amp; Plants in days.<br>Plant Roots will settle into soil which stays contained.<br>Live Aquatic Plants &amp; Soil are Key to a <span class="highlight">THRIVING</span> Freshwater Aquarium.</p>
    <p class="contact-line">www.rootcrateaquatics.com | info@rootcrateaquatics.com</p>
    <p class="slogan">STAY <span class="slogan-accent">RIVER</span> CALM</p>
  </section>
</main>
</body>
</html>
```